Design business card for new business which advocates for elders in nursing homes or personal care h

New business for rights of the elderly residents who reside in personal care homes and or nursing homes. I am looking for a business card with logo of keystone for Pennsylvania and something in side the keystone that represents healthcare, advocates, something on that line; monitor care received and needs of resident. Chart audits, State Regulation compliance

Target Market(s)

Seniors no longer safe to live at home by themselves along with their kids

Industry/Entity Type

Business

Contact Information for Business Card

Keystone symbol to represent Pensylvaoa with some kind of symbol inside to represent advocate, seniors, or healthcare symbol

Font styles to use
Serif

Colors
33a6d7
85cae6
abd037

Requirements
Must have
• Brightwell Elder Allies is our business name; our tag line is Path to Better Living
Nice to have
• Nice logo

```html
<!DOCTYPE html>
<html lang="en">
<head>
<meta charset="utf-8">
<title>Brightwell Elder Allies — Business Card</title>
<link href="https://fonts.googleapis.com/css2?family=Tinos:wght@400;700&display=swap" rel="stylesheet">
<style>
  :root {
    --page: #e9e7e3;
    --card: #ffffff;
    --card-shade: #eeeeee;
    --blue: #33a6d7;
    --blue-light: #4cc6e4;
    --ink: #1c1c1c;
    --ink-soft: #3a3a3a;
    --rule: #b9b9b9;
  }
  * { box-sizing: border-box; margin: 0; padding: 0; }
  html, body {
    width: 1200px; height: 892px; overflow: hidden;
    background: var(--page);
    font-family: "Tinos", "Times New Roman", serif;
    color: var(--ink);
  }
  .business-card {
    position: absolute; left: 100px; top: 166px;
    width: 1000px; height: 560px;
    background: linear-gradient(100deg, var(--card) 40%, var(--card-shade) 100%);
    box-shadow: 0 18px 40px rgba(0,0,0,.25);
    overflow: hidden;
  }
  .brand-panel {
    position: absolute; left: 0; top: 0; width: 370px; height: 100%;
    background: linear-gradient(160deg, var(--blue) 0%, var(--blue-light) 100%);
  }
  .corner-fold { position: absolute; left: 0; bottom: 0; }
  .logo-lockup {
    position: absolute; left: 60px; top: 250px; width: 250px;
    display: flex; align-items: center; gap: 14px;
    color: #ffffff; font-weight: 700; font-size: 26px; line-height: 1.15;
  }
  .logo-square { width: 34px; height: 34px; background: #ffffff; flex: none; }
  .contact-icons { position: absolute; left: 318px; top: 0; }
  .company-heading { position: absolute; left: 405px; top: 40px; }
  .company-name { font-size: 66px; font-weight: 700; line-height: 1; letter-spacing: 1px; }
  .company-sub { font-size: 40px; font-weight: 700; line-height: 1.1; letter-spacing: 1px; }
  .tagline { font-size: 22px; letter-spacing: 2px; color: var(--ink-soft); margin-top: 4px; }
  .person { position: absolute; left: 405px; top: 205px; }
  .person-accent { position: absolute; left: -6px; top: 58px; width: 60px; height: 4px; background: var(--blue); }
  .person-name { font-size: 36px; font-weight: 700; padding-left: 70px; }
  .person-title { font-size: 19px; color: var(--ink-soft); padding-left: 70px; margin-top: 2px; }
  .contact-list { position: absolute; left: 405px; top: 300px; right: 0; list-style: none; }
  .contact-list li {
    height: 62px; padding-top: 18px; padding-left: 10px;
    font-size: 22px; letter-spacing: .5px;
    border-bottom: 1px solid var(--rule);
  }
</style>
</head>
<body>
  <article class="business-card">
    <div class="brand-panel">
      <svg class="corner-fold" width="170" height="140" viewBox="0 0 170 140" aria-hidden="true">
        <polygon points="0,0 0,140 170,140" fill="#f3f3f3"/>
      </svg>
      <div class="logo-lockup">
        <span class="logo-square"></span>
        <span>Brightwell Elder Allies</span>
      </div>
    </div>

    <svg class="contact-icons" width="60" height="560" viewBox="0 0 60 560" aria-hidden="true">
      <g fill="none" stroke="#ffffff" stroke-width="2">
        <circle cx="26" cy="393" r="20"/>
        <path d="M18 385c2 8 8 14 16 16l3-4-5-3-3 2c-3-2-5-4-7-7l2-3-3-5z" fill="#ffffff" stroke="none"/>
        <circle cx="26" cy="455" r="20"/>
        <rect x="16" y="446" width="20" height="15" rx="1"/>
        <line x1="22" y1="465" x2="30" y2="465"/>
        <circle cx="26" cy="517" r="20"/>
        <rect x="16" y="509" width="20" height="15"/>
        <polyline points="16,509 26,518 36,509"/>
      </g>
    </svg>

    <header class="company-heading">
      <h1 class="company-name">Brightwell</h1>
      <p class="company-sub">Elder Allies</p>
      <p class="tagline">Path to Better Living</p>
    </header>

    <div class="person">
      <span class="person-accent"></span>
      <p class="person-name">Employee name</p>
      <p class="person-title">Managing Director</p>
    </div>

    <ul class="contact-list">
      <li>Suite 4 Maple Row Ave Harmon,PA 00000</li>
      <li>055-3190 2277</li>
      <li>www.brightwellallies.com</li>
      <li>hello@brightwellallies.com</li>
    </ul>
  </article>
</body>
</html>
```